Valmuna - Plant extraction for human use

Valmuna is a plant extraction based on long pepper containing a high concentration of piperlongumine. Piperlongumine has mainly anti-cancer properties, shown in many animal studies (200). It has as well shown to inhibit dementia and bone inflammation (in animal studies). We are the first to offer this extract for the European market. Because the product will be sold under a ‘plant extraction’ legislation, we cannot make any claims about the medical properties of the extract. I need a design for the packaging (blister pack) in a category for life enhancing medicine with no connotation of cancer for the European market in a first phase. We target people from 35-75 years old. For the younger group of people, we would propose (without saying) to use our product for chemoprevention against cancer. For those patients which have been diagnosed with cancer, we would propose to use it in conjunction with chemo-radio or immunotherapy (without saying).
Target Market(s)
Europe
Look and feel

```html
<!DOCTYPE html>
<html lang="en">
<head>
<meta charset="utf-8">
<title>Piperlongumine – Package Front</title>
<link href="https://fonts.googleapis.com/css2?family=Josefin+Sans:wght@300;700&display=swap" rel="stylesheet">
<style>
  :root {
    --bg: #eceee6;
    --leaf: #abd135;
    --leaf-deep: #9cc12c;
    --white: #ffffff;
    --ink: #0c0c0c;
  }
  * { margin: 0; padding: 0; box-sizing: border-box; }
  html, body { width: 1200px; height: 1200px; overflow: hidden; }
  body {
    background: var(--bg);
    display: flex;
    align-items: center;
    justify-content: center;
    font-family: "Josefin Sans", sans-serif;
  }
  .pack-front {
    position: relative;
    width: 1000px;
    height: 620px;
    background: var(--leaf);
    overflow: hidden;
  }
  .molecule-art {
    position: absolute;
    left: 30px;
    top: 90px;
    width: 560px;
    height: 480px;
    border-radius: 40px;
    background: radial-gradient(ellipse at center, var(--leaf-deep) 0%, var(--leaf) 70%);
  }
  .tablet-count {
    position: absolute;
    right: 80px;
    top: 150px;
    color: var(--white);
    font-weight: 300;
    font-size: 48px;
    letter-spacing: 1px;
  }
  .name-band {
    position: absolute;
    left: 0;
    top: 230px;
    width: 100%;
    height: 130px;
    background: var(--white);
    display: flex;
    align-items: center;
    padding-left: 120px;
  }
  .product-name {
    color: var(--ink);
    font-weight: 700;
    font-size: 76px;
    letter-spacing: 4px;
    line-height: 1;
    padding-top: 10px;
  }
  .source-line {
    position: absolute;
    left: 390px;
    top: 395px;
    color: var(--ink);
    font-weight: 300;
    font-size: 36px;
  }
  .quality-badge {
    position: absolute;
    right: 90px;
    bottom: 50px;
    width: 130px;
    height: 130px;
    border: 4px solid var(--white);
    border-radius: 50%;
  }
</style>
</head>
<body>
  <main class="pack-front">
    <div class="molecule-art" role="img" aria-label="Line drawing of the piperlongumine molecular structure"></div>
    <p class="tablet-count">36 tablets</p>
    <div class="name-band">
      <h1 class="product-name">PIPERLONGUMINE</h1>
    </div>
    <p class="source-line">Piper longum extract</p>
    <div class="quality-badge" role="img" aria-label="Natural ingredients badge"></div>
  </main>
</body>
</html>
```